Business card design for web travel company

Hi
we'd like to receive some proposal for a business card design.
Quindra is a private travel club, dedicated to all travel lovers, with unique offers for exclusive destinations all around the world. At Quindra you can find a wide range of offers for resorts, boutique hotels and travel packages at the best guaranteed price available on the market. The convenience of the offer is guaranteed by a private sales model: offers are available for a limited time only and they are personally chosen by Quindra's qualified team of travel experts.
We offer only exclusive hotels with discounted prices but we are not an outlet or a discount supermarket: the design should reflect our connection with luxury, exclusivity using the same style of our website www.quindra-example.com.
We want to make sure that when we'll present ourself to our business partner they will feel immediately which is our brand positioning giving them also a sense of an affordable and reliable partner.
In attachment you can also find our brand guidelines (please note that we are NOT USING ANY MORE THE TAG LINE "Five star outlet" mentioned in it).
The info to be inserted are:
Name Surname
Job Title
Tel
Mobile (when needed)
Email
Quindra S.r.l.
Via Pietro Lanzi 27
20137 Milano

```html
<!DOCTYPE html>
<html lang="en">
<head>
<meta charset="utf-8">
<title>Quindra – Business Card</title>
<link href="https://fonts.googleapis.com/css2?family=Carlito:wght@400;700&display=swap" rel="stylesheet">
<style>
  :root {
    --page: #ffffff;
    --card: #060606;
    --stripe: rgba(255,255,255,0.035);
    --lime: #c4c400;
    --lime-deep: #6f6e06;
    --lime-light: #f2f27a;
    --lime-text: #b4b62c;
    --white: #ffffff;
    --panel: #0c0c06;
  }
  html, body {
    margin: 0;
    width: 1200px;
    height: 900px;
    overflow: hidden;
    background: var(--page);
    font-family: "Carlito", "Calibri", sans-serif;
  }
  .canvas { position: relative; width: 1200px; height: 900px; }
  .card {
    position: absolute;
    top: 295px;
    width: 544px;
    height: 310px;
    overflow: hidden;
    background:
      repeating-linear-gradient(120deg, var(--stripe) 0 1px, transparent 1px 7px),
      var(--card);
    box-shadow: 0 1px 4px rgba(0,0,0,0.35);
  }
  .card--front { left: 29px; }
  .card--back { left: 627px; }

  .brand-band {
    position: absolute;
    left: 0; top: 330px; width: 544px; height: 182px;
    top: 35px;
  }
  .brand-panel {
    position: absolute;
    left: 73px; top: 58px;
    width: 398px; height: 122px;
    background: radial-gradient(ellipse at 50% 45%, #2a2a10 0%, var(--panel) 70%);
    box-shadow: 0 0 6px rgba(0,0,0,0.7), inset 0 0 0 1px rgba(200,200,60,0.25);
    display: flex; align-items: center; justify-content: center;
  }
  .brand-name {
    color: var(--white);
    font-size: 78px;
    font-weight: 400;
    letter-spacing: 2px;
    line-height: 1;
  }
  .front-contact {
    position: absolute;
    left: 0; right: 0; top: 253px;
    text-align: center;
    color: var(--lime-text);
    font-size: 15px;
    line-height: 21px;
  }
  .front-contact .sep { margin: 0 6px; }

  .contact-list {
    list-style: none;
    margin: 0; padding: 0;
    position: absolute;
    left: 37px; top: 178px;
  }
  .contact-list li {
    display: flex; align-items: center;
    height: 36px;
    color: var(--white);
    font-size: 18px;
  }
  .contact-list .marker {
    width: 17px; height: 17px;
    margin-right: 10px;
    background: linear-gradient(135deg, var(--lime-light), var(--lime) 55%, var(--lime-deep));
  }
</style>
</head>
<body>
<div class="canvas">
  <section class="card card--front">
    <svg class="brand-band" width="544" height="182" viewBox="0 0 544 182">
      <defs>
        <linearGradient id="bandFill" x1="0" y1="0" x2="1" y2="0">
          <stop offset="0" stop-color="#a8a806"/>
          <stop offset="0.5" stop-color="#8d8c06"/>
          <stop offset="1" stop-color="#c8c800"/>
        </linearGradient>
        <linearGradient id="edgeFill" x1="0" y1="0" x2="1" y2="0">
          <stop offset="0" stop-color="#d8d820"/>
          <stop offset="1" stop-color="#f4f46a"/>
        </linearGradient>
      </defs>
      <rect x="0" y="0" width="544" height="182" fill="url(#bandFill)"/>
      <polygon points="0,0 544,0 544,8 0,4" fill="url(#edgeFill)"/>
      <polygon points="0,170 544,166 544,176 0,182" fill="url(#edgeFill)"/>
    </svg>
    <div class="brand-panel"><span class="brand-name">Quindra</span></div>
    <div class="front-contact">
      <div>Quindra S.r.l., Via Pietro Lanzi 27, 20137 Milano</div>
      <div>M. 1234567890<span class="sep">•</span>E. info@quindra-example.com</div>
    </div>
  </section>

  <section class="card card--back">
    <ul class="contact-list">
      <li><span class="marker"></span>Quindra S.r.l., Via Pietro Lanzi 27, 20137 Milano</li>
      <li><span class="marker"></span>M. 1234567890</li>
      <li><span class="marker"></span>E. info@quindra-example.com</li>
    </ul>
  </section>
</div>
</body>
</html>
```